Hip surgeon needs a stationery design

I need a new stationery design for my private practice.
My practice is focused in hip arthroplasty (hip prosthesis).
I'd like to see designs most in blue or shades of blue.
I've uploaded my new logo to help with the task.
Also, I'm a member of some societies and I've uploaded their logos either, so I'd like to see them in some of the stationeries.
Itens list:
business card
letterhead A4
envelope
prescription block A5
one fold for A4 (please see the archive "pocket")
Personal data:
Dr. Renan L. Vasconti
CRM/PR 57316
site: www.clinicapelvora.com.br
email: dr.renan@clinicapelvora.com.br
Adress:
Rua Leopoldo Marques Vieira de Lima, 712
Campo Sereno - Curitiba/PR
41 30875316 I 30875317
Updates
I forgot to mention that my practice is focused primarily in hip arthroplasty (total hip prosthesis) and the target audience range from young adults to the elderly.
I also perform hip preserving surgeries (open and arthroscopic procedures) and pelvic and hip fracture surgery (trauma).
- Any "cleaner" fonts are welcome

```html
<!DOCTYPE html>
<html lang="pt-BR">
<head>
<meta charset="utf-8">
<title>Dr. Renan L. Vasconti — Cartão de visita</title>
<link href="https://fonts.googleapis.com/css2?family=Open+Sans:wght@400;600&display=swap" rel="stylesheet">
<style>
  :root {
    --backdrop: #bcd5e6;
    --card-navy: #0f2a4a;
    --card-navy-deep: #0c2440;
    --accent-blue: #4aa3e8;
    --accent-soft: #3a7fc0;
    --text-white: #ffffff;
    --text-muted: #a9c4df;
  }
  * { box-sizing: border-box; margin: 0; padding: 0; }
  html, body {
    width: 1200px; height: 1000px; overflow: hidden;
    background: var(--backdrop);
    font-family: "Open Sans", Arial, sans-serif;
  }
  .canvas {
    width: 1200px; height: 1000px;
    display: flex; flex-direction: column; align-items: center; justify-content: center;
    gap: 70px;
  }
  .card {
    position: relative;
    width: 620px; height: 354px;
    background: linear-gradient(160deg, var(--card-navy) 0%, var(--card-navy-deep) 100%);
    box-shadow: 0 4px 0 var(--accent-blue), 0 14px 30px rgba(20, 50, 80, 0.25);
  }
  /* back side */
  .card-back { display: flex; align-items: center; justify-content: center; gap: 16px; }
  .brand-dot {
    width: 46px; height: 46px; border-radius: 50%;
    background: var(--accent-soft);
    flex: none;
  }
  .card-back .brand-name { font-size: 26px; font-weight: 400; color: var(--accent-soft); }

  /* front side */
  .brand-lockup {
    position: absolute; top: 56px; right: 44px;
    display: flex; align-items: center; gap: 10px;
  }
  .brand-lockup .brand-dot { width: 34px; height: 34px; background: var(--accent-blue); }
  .brand-lockup .brand-name { font-size: 21px; font-weight: 400; color: var(--accent-blue); }

  .holder { position: absolute; left: 44px; top: 148px; }
  .holder-name { font-size: 24px; font-weight: 400; color: var(--text-white); line-height: 1.2; }
  .holder-reg { font-size: 16px; color: var(--accent-soft); margin-top: 2px; }

  .divider {
    position: absolute; left: 44px; right: 44px; top: 220px;
    height: 1px; background: var(--accent-blue);
  }

  .contact-list { position: absolute; list-style: none; font-size: 9.5px; color: var(--text-muted); }
  .contact-list li { display: flex; align-items: center; gap: 6px; line-height: 17px; }
  .contact-list svg { width: 9px; height: 9px; flex: none; }
  .contact-left { left: 44px; top: 230px; }
  .contact-right { right: 44px; top: 178px; }
</style>
</head>
<body>
<main class="canvas">

  <section class="card card-back" aria-label="Verso do cartão">
    <span class="brand-dot"></span>
    <span class="brand-name">Dr. Renan L. Vasconti</span>
  </section>

  <section class="card card-front" aria-label="Frente do cartão">
    <div class="brand-lockup">
      <span class="brand-dot"></span>
      <span class="brand-name">Dr. Renan L. Vasconti</span>
    </div>

    <div class="holder">
      <p class="holder-name">Dr. Renan L. Vasconti</p>
      <p class="holder-reg">CRM/PR 57316</p>
    </div>

    <div class="divider"></div>

    <ul class="contact-list contact-left">
      <li>
        <svg viewBox="0 0 10 10"><circle cx="5" cy="5" r="5" fill="#4aa3e8"/><path d="M5 2.2a1.8 1.8 0 0 0-1.8 1.8C3.2 5.4 5 7.8 5 7.8S6.8 5.4 6.8 4A1.8 1.8 0 0 0 5 2.2z" fill="#0f2a4a"/></svg>
        Rua Leopoldo Marques Vieira de Lima, 712 Campo Sereno - Curitiba/PR
      </li>
      <li>
        <svg viewBox="0 0 10 10"><circle cx="5" cy="5" r="5" fill="#4aa3e8"/><path d="M3.3 2.6l1 1-.6.7c.4.8 1 1.4 1.8 1.8l.7-.6 1 1-.7.8C4.8 7.1 2.9 5.2 2.6 3.3z" fill="#0f2a4a"/></svg>
        41 30875316 I 30875317
      </li>
    </ul>

    <ul class="contact-list contact-right">
      <li>
        <svg viewBox="0 0 10 10"><circle cx="5" cy="5" r="5" fill="#4aa3e8"/><circle cx="5" cy="5" r="2.4" fill="none" stroke="#0f2a4a" stroke-width="0.8"/></svg>
        www.clinicapelvora.com.br
      </li>
      <li>
        <svg viewBox="0 0 10 10"><circle cx="5" cy="5" r="5" fill="#4aa3e8"/><rect x="2.6" y="3.3" width="4.8" height="3.4" fill="none" stroke="#0f2a4a" stroke-width="0.8"/><path d="M2.6 3.3L5 5.2l2.4-1.9" fill="none" stroke="#0f2a4a" stroke-width="0.8"/></svg>
        dr.renan@clinicapelvora.com.br
      </li>
    </ul>
  </section>

</main>
</body>
</html>
```